Livestock Consulting Company has a logo but needs business cards and a uniform logo

My company works with farmers advising them on managing cattle and sheep. I have a logo but need business cards and a version of my logo to go onto my work shirts. I need the following wording added to my logo for my shirts "Marlowby Livestock Consulting".

```html
<!DOCTYPE html>
<html lang="en">
<head>
<meta charset="utf-8">
<title>Marlowby Livestock Consulting – Business Cards</title>
<link rel="stylesheet" href="https://fonts.googleapis.com/css2?family=Marcellus&family=Lato:wght@400;700&display=swap">
<style>
  :root {
    --brown: #7f6448;
    --white: #ffffff;
    --ink: #1e1a16;
    --stage: #1b1b1b;
  }
  * { margin: 0; padding: 0; box-sizing: border-box; }
  html, body {
    width: 1200px;
    height: 1015px;
    overflow: hidden;
    background: var(--stage);
  }
  .card {
    position: absolute;
    width: 560px;
    height: 320px;
    overflow: hidden;
    box-shadow: 0 14px 30px rgba(0,0,0,0.55);
  }

  .brand-name {
    font-family: "Marcellus", serif;
    font-weight: 400;
    text-transform: uppercase;
    line-height: 1.1;
  }
  .brand-main {
    display: block;
    font-size: 36px;
    letter-spacing: 2px;
  }
  .brand-sub {
    display: block;
    font-size: 12px;
    letter-spacing: 5px;
    margin-top: 4px;
  }
  .brand-dot {
    border-radius: 50%;
    flex: none;
  }

  /* Back of card */
  .card-back {
    left: 90px;
    top: 130px;
    background: var(--brown);
    display: flex;
    align-items: center;
    justify-content: center;
    gap: 22px;
    color: var(--white);
  }
  .card-back .brand-dot {
    width: 64px;
    height: 64px;
    background: var(--white);
  }
  .card-back .brand-divider {
    width: 1px;
    height: 76px;
    background: var(--white);
    opacity: 0.8;
  }

  /* Front of card */
  .card-front {
    left: 550px;
    top: 560px;
    background: var(--white);
  }
  .card-front .wave {
    position: absolute;
    inset: 0;
    width: 560px;
    height: 320px;
  }
  .front-brand {
    position: absolute;
    left: 40px;
    top: 58px;
    color: var(--brown);
  }
  .front-brand .brand-dot {
    display: block;
    width: 58px;
    height: 58px;
    background: var(--brown);
    margin: 0 0 12px 52px;
  }
  .front-brand .brand-main { font-size: 30px; }
  .front-brand .brand-sub { font-size: 10px; letter-spacing: 4.5px; }

  .person {
    position: absolute;
    right: 34px;
    top: 26px;
    text-align: right;
  }
  .person-name {
    font-family: "Marcellus", serif;
    font-size: 22px;
    letter-spacing: 1.5px;
    color: var(--brown);
    text-transform: uppercase;
    line-height: 1.2;
  }
  .person-role {
    font-family: "Lato", sans-serif;
    font-size: 13px;
    color: var(--ink);
    letter-spacing: 0.5px;
    margin-top: 2px;
  }

  .contact-list {
    position: absolute;
    right: 26px;
    top: 150px;
    list-style: none;
    font-family: "Lato", sans-serif;
    font-size: 14px;
    color: var(--white);
    text-align: right;
    line-height: 22px;
  }
  .contact-list li {
    display: flex;
    justify-content: flex-end;
    align-items: flex-start;
    gap: 8px;
  }
  .contact-list .icon {
    width: 14px;
    height: 14px;
    margin-top: 4px;
    flex: none;
  }
  .contact-list .address { margin-top: 6px; }
</style>
</head>
<body>

<section class="card card-back" aria-label="Business card back">
  <span class="brand-dot" aria-hidden="true"></span>
  <span class="brand-divider" aria-hidden="true"></span>
  <h1 class="brand-name">
    <span class="brand-main">Marlowby</span>
    <span class="brand-sub">Livestock Consulting</span>
  </h1>
</section>

<section class="card card-front" aria-label="Business card front">
  <svg class="wave" viewBox="0 0 560 320" aria-hidden="true">
    <path d="M0 268 C160 250,240 238,300 178 S440 108,560 100" fill="none" stroke="var(--brown)" stroke-width="5"/>
    <path d="M0 286 C160 268,240 256,300 196 S440 126,560 118 L560 320 L0 320 Z" fill="var(--brown)"/>
  </svg>

  <div class="front-brand">
    <span class="brand-dot" aria-hidden="true"></span>
    <h2 class="brand-name">
      <span class="brand-main">Marlowby</span>
      <span class="brand-sub">Livestock Consulting</span>
    </h2>
  </div>

  <div class="person">
    <p class="person-name">Edwin Carrow</p>
    <p class="person-role">Managing Director</p>
  </div>

  <ul class="contact-list">
    <li>044-555 019 274
      <svg class="icon" viewBox="0 0 16 16" aria-hidden="true"><path d="M3 1 L6 1 L7 5 L5 6.5 C6 9 7 10 9.5 11 L11 9 L15 10 L15 13 C15 14 14 15 13 15 C6 14.5 1.5 10 1 3 C1 2 2 1 3 1 Z" fill="var(--white)"/></svg>
    </li>
    <li>hello@marlowby.co
      <svg class="icon" viewBox="0 0 16 16" aria-hidden="true"><rect x="1" y="3" width="14" height="10" fill="var(--white)"/><path d="M1 3 L8 9 L15 3" fill="none" stroke="var(--brown)" stroke-width="1.2"/></svg>
    </li>
    <li>www.marlowbyfarm.co
      <svg class="icon" viewBox="0 0 16 16" aria-hidden="true"><circle cx="8" cy="8" r="7" fill="var(--white)"/><g fill="none" stroke="var(--brown)" stroke-width="0.9"><ellipse cx="8" cy="8" rx="3" ry="7"/><line x1="1" y1="8" x2="15" y2="8"/><line x1="2" y1="4.5" x2="14" y2="4.5"/><line x1="2" y1="11.5" x2="14" y2="11.5"/></g></svg>
    </li>
    <li class="address">18 Fenwick Lane, Hollis<br>Northdale, 40817
      <svg class="icon" viewBox="0 0 16 16" aria-hidden="true"><path d="M8 15 C4 10 3 8 3 6 A5 5 0 0 1 13 6 C13 8 12 10 8 15 Z" fill="var(--white)"/><circle cx="8" cy="6" r="2" fill="var(--brown)"/></svg>
    </li>
  </ul>
</section>

</body>
</html>
```